Flyer-Design für Tanzschule
Zielgruppe
Tanzschule
Aufgabenstellung
Ich möchte ein Banner zur Werbung auf Plauderwand für eine Tanzveranstaltung so oder so ähnlich wie dieses Bild bildschirmfoto_2022_08_03_um_02.35.52.png.
Eines (oder mehrere) dieser Bilder sollte anstelle der Personen sein:
Der DJ sollte in Klein mit darauf:
bild_marek_dj.jpg (DJ Marek)
Folgende Logos sollen mit darauf. (Wichtigstes als erstes)
bildschirmfoto_2022_08_04_um_15.39.02.png (Original ohne weißen Hintergrund kann ich nachträglich darauf setzen. Ich habe es aktuell noch nicht)
Folgende Informationen sollen enthalten sein. (Wichtigste als erstes)
Bachata, Kizomba & Salsa Fiesta
Jeden Mittwoch 21:00 - 01:00 Uhr
La Gaviota - Käthnerweg 7, 79112 Freiburg im Breisgau
5€ Verzehrbon / Kein Eintritt

```html
<!DOCTYPE html>
<html lang="de">
<head>
<meta charset="utf-8">
<title>Bachata Kizomba Salsa Fiesta – Banner</title>
<link href="https://fonts.googleapis.com/css2?family=Oswald:wght@300;500;700&family=Kaushan+Script&display=swap" rel="stylesheet">
<style>
  :root {
    --page: #ffffff;
    --mist: #e2dee1;
    --rose-light: #dcb4c8;
    --rose: #c98fb0;
    --rose-deep: #b9558f;
    --magenta: #d8397c;
    --berry: #a3185f;
    --white: #ffffff;
    --ink: #3a3a3a;
    --fiesta-start: #c8145e;
    --fiesta-end: #f7853e;
  }
  * { margin: 0; padding: 0; box-sizing: border-box; }
  html, body {
    width: 1200px; height: 960px; overflow: hidden;
    background: var(--page);
  }
  .banner {
    position: absolute; left: 0; top: 142px;
    width: 1200px; height: 675px; overflow: hidden;
    background: linear-gradient(180deg, var(--mist) 0%, var(--mist) 45%, var(--rose) 75%, var(--rose-deep) 100%);
    font-family: "Oswald", sans-serif;
  }
  .backdrop { position: absolute; inset: 0; width: 1200px; height: 675px; }

  .partner-logos { position: absolute; left: 46px; top: 30px; display: flex; gap: 26px; align-items: center; z-index: 3; }
  .venue-mark { display: flex; flex-direction: column; align-items: center; gap: 6px; }
  .venue-mark .dot { width: 22px; height: 22px; border-radius: 50%; background: var(--ink); }
  .venue-mark span, .school-mark span {
    font-weight: 500; color: var(--ink); font-size: 11px; letter-spacing: 0.5px;
  }
  .school-mark span { display: block; font-size: 16px; line-height: 19px; letter-spacing: 0; }

  .dancers-photo {
    position: absolute; left: 30px; top: 40px; width: 620px; height: 635px;
    background: radial-gradient(ellipse 50% 52% at 55% 48%,
      #fbf4f7 0%, #f2d3e2 28%, #e6a9cb 52%, #c96f9f 72%, rgba(201,111,159,0.35) 88%, rgba(201,111,159,0) 100%);
  }
  .dj-photo {
    position: absolute; left: 0; top: 558px; width: 182px; height: 117px;
    background: linear-gradient(180deg, #9c7f8d 0%, #d9b2ba 38%, #ecc9cf 62%, #f1d9e0 100%);
  }
  .dj-credit {
    position: absolute; left: 196px; top: 628px;
    font-weight: 500; font-size: 20px; color: var(--white); letter-spacing: 0.2px;
  }
  .dj-credit em { font-style: normal; font-weight: 300; color: #a5407e; }

  .event-info { position: absolute; left: 700px; top: 46px; width: 440px; text-align: center; }
  .schedule { font-size: 30px; line-height: 40px; white-space: nowrap; }
  .schedule .day { font-weight: 300; color: var(--white); }
  .schedule .time { font-weight: 500; color: var(--berry); }

  .dance-list { position: absolute; left: 700px; top: 82px; width: 440px; }
  .dance-list span {
    display: block; font-weight: 700; color: var(--white);
    text-align: center; letter-spacing: -3px; line-height: 1;
  }
  .dance-list .bachata { font-size: 150px; line-height: 128px; transform: scaleX(0.72); }
  .dance-list .kizomba { font-size: 150px; line-height: 128px; transform: scaleX(0.66); }
  .dance-list .salsa   { font-size: 200px; line-height: 176px; transform: scaleX(0.78); }

  .fiesta {
    position: absolute; left: 740px; top: 250px; width: 400px; text-align: center;
    font-family: "Kaushan Script", cursive; font-size: 150px; line-height: 180px;
    background: linear-gradient(90deg, var(--fiesta-start), var(--fiesta-end));
    -webkit-background-clip: text; background-clip: text; color: transparent;
    transform: rotate(-4deg);
  }

  .venue { position: absolute; left: 700px; top: 526px; width: 440px; text-align: center; }
  .venue-name { font-weight: 500; font-size: 52px; line-height: 58px; color: var(--berry); }
  .venue-address { font-weight: 300; font-size: 24px; line-height: 32px; color: var(--white); white-space: nowrap; }
  .venue-offer { font-weight: 500; font-size: 19px; line-height: 28px; color: var(--white); }
</style>
</head>
<body>
  <main class="banner">
    <svg class="backdrop" viewBox="0 0 1200 675" aria-hidden="true">
      <path d="M0 0 H283 C260 30 200 15 150 50 C110 80 90 115 40 115 C15 115 0 105 0 100 Z" fill="#c48fae"/>
      <path d="M506 0 H940 C930 40 880 60 800 40 C720 25 700 70 620 70 C560 70 520 40 506 0 Z" fill="#dcb4c8"/>
      <path d="M1200 90 C1160 110 1150 160 1150 230 C1150 300 1100 330 1080 400 C1060 470 1110 520 1160 580 C1180 610 1200 620 1200 620 Z" fill="#c98fb0" opacity="0.8"/>
      <path d="M0 400 C50 360 120 355 160 380 C205 410 185 460 150 500 C120 540 80 560 0 560 Z" fill="#c27ba5" opacity="0.7"/>
    </svg>

    <div class="dancers-photo" role="img" aria-label="Foto eines Tanzpaares in Bachata-Pose mit leuchtenden Lichtschweifen"></div>

    <svg class="backdrop" viewBox="0 0 1200 675" aria-hidden="true">
      <path d="M120 675 C140 600 190 555 250 550 C320 545 360 590 400 620 C440 650 470 660 480 675 Z" fill="#d8397c"/>
    </svg>

    <div class="partner-logos">
      <div class="venue-mark"><i class="dot"></i><span>LA GAVIOTA</span></div>
      <div class="school-mark"><span>Tanzschule</span><span>Ritmo Claro</span></div>
    </div>

    <div class="dj-photo" role="img" aria-label="Foto von DJ Marek mit Kopfhörern"></div>
    <p class="dj-credit">DJ MAREK <em>LIVE</em></p>

    <div class="event-info">
      <p class="schedule"><span class="day">JEDEN MITTWOCH</span> <span class="time">21:00 - 01:00 UHR</span></p>
    </div>

    <h1 class="dance-list">
      <span class="bachata">BACHATA</span>
      <span class="kizomba">KIZOMBA</span>
      <span class="salsa">SALSA</span>
    </h1>
    <p class="fiesta">Fiesta</p>

    <div class="venue">
      <p class="venue-name">LA GAVIOTA</p>
      <p class="venue-address">KÄTHNERWEG 7, 79112 FREIBURG IM BREISGAU</p>
      <p class="venue-offer">5€ VERZEHRBON / KEIN EINTRITT</p>
    </div>
  </main>
</body>
</html>
```